Social Media Templates for Ambervale Kinship

We need a set of Square (1080 x 1080) social media posts.

My company works with sports clubs, helping them to raise money with a lottery.

I need a set of social media image that I can use to appeal to new Ambervale Kinship to encourage them to start a lottery with us.

This landing page has worked very well for us https://ambervalekinship.com/ambervale-kinship/

THING THAT APPEAL TO CLUBS

No Setup Fees/Start for Free - (We don’t charge any registration fees, or setup fees so you can start raising money from the first draw.)

Start Straight Away - (A club can start raising money straight away.)

Sustainable Income - (The average player plays for 7 years)

Subscription Lottery - (once a player joins, they play until the choose to leave. A club doesn't have to sell tickets every draw to the same people)

All Administration Taken Care Of - (We do all the hard work, so they can focus on running their club.)

Unlimited Income - (There is no limit on the amount of money a club can raise: the more players, the more funds for the club.)

Fundraising reach - (Reach new fans)

50% of the sales is guaranteed profit

£25,000 jackpot - (a person could win £25,000 every week)

Price - (It costs just £1 per week to enter)

Help Your Club - (100% of the profit goes to the club who a player chooses to support)

You can see all the clubs we work with on www.ambervalekinship.com

The images will also be used on Facebook. You can see some examples here https://www.friendvista.com/AmbervaleKinship/ (you may need a proxy to view this page as it is only viewable in the UK, so I have attached some screenshots)

You can find the Ambervale Kinship Logo here https://www.logocrate.com/quillmarshco/

Target Market(s)

People who are involved with amateur sports in United Kingdom

Industry/Entity Type

Gambling

Font styles to use
Sans Serif

Requirements
Must have
• My project must look great on social social media and encourage people to get in touch about starting a lottery with us.

Adobe Suite files must be provided

```html
<!DOCTYPE html>
<html lang="en">
<head>
<meta charset="utf-8">
<title>Ambervale Kinship – Social Post</title>
<link rel="stylesheet" href="https://fonts.googleapis.com/css2?family=Arimo:wght@400;700&family=Bebas+Neue&family=Gochi+Hand&family=Montserrat:wght@700;800&display=swap">
<style>
  :root {
    --panel: #ece9f3;
    --blue: #2c7fc0;
    --amber: #fdb300;
    --ink: #1d1d1f;
    --night: #0b1222;
    --stadium: #2f86d6;
    --pitch: #2f6a24;
    --white: #ffffff;
  }
  * { margin: 0; padding: 0; box-sizing: border-box; }
  html, body { width: 1200px; height: 1200px; overflow: hidden; background: var(--panel); }
  .post { position: relative; width: 1200px; height: 1200px; overflow: hidden; }
  .post-shapes { position: absolute; inset: 0; }
  .brand-name {
    position: absolute; left: 102px; top: 110px; width: 247px;
    font-family: "Bebas Neue", sans-serif; color: var(--white);
    font-size: 58px; line-height: 0.95; text-align: center;
  }
  .feature { position: absolute; right: 41px; text-align: right; }
  .feature-title {
    font-family: "Arimo", sans-serif; font-weight: 700; color: var(--blue);
    font-size: 66px; line-height: 1; letter-spacing: 0.5px;
  }
  .feature-note {
    font-family: "Arimo", sans-serif; font-weight: 400; color: var(--ink);
    font-size: 28px; line-height: 1; margin-top: 12px;
  }
  .feature--start { top: 52px; }
  .feature--income { top: 204px; }
  .feature--income .feature-note { margin-right: 6px; }
  .divider { position: absolute; left: 673px; top: 334px; width: 486px; height: 3px; background: var(--amber); }
  .reach-title {
    position: absolute; right: 40px; top: 392px;
    font-family: "Bebas Neue", sans-serif; color: var(--blue);
    font-size: 98px; line-height: 0.9;
  }
  .profit-figure {
    position: absolute; left: 583px; top: 512px;
    font-family: "Bebas Neue", sans-serif; color: var(--ink);
    font-size: 122px; line-height: 1;
  }
  .profit-figure sup { font-size: 60px; vertical-align: 48px; }
  .profit-text {
    position: absolute; left: 740px; top: 518px;
    font-family: "Montserrat", sans-serif; font-weight: 800; color: var(--ink);
    font-size: 40px; line-height: 1.05; letter-spacing: 0.5px;
  }
  .jackpot-amount {
    position: absolute; right: 48px; top: 680px;
    font-family: "Montserrat", sans-serif; font-weight: 800; color: var(--blue);
    font-size: 112px; line-height: 1;
  }
  .jackpot-amount sup { font-size: 52px; vertical-align: 46px; margin-right: 4px; }
  .jackpot-label {
    position: absolute; right: 40px; top: 785px;
    font-family: "Gochi Hand", cursive; color: var(--amber);
    font-size: 100px; line-height: 1; letter-spacing: 6px;
  }
  .entry-price {
    position: absolute; right: 41px; top: 890px;
    font-family: "Arimo", sans-serif; font-weight: 700; color: var(--blue);
    font-size: 30px; line-height: 1;
  }
  .entry-price sup { font-size: 16px; }
  .cta {
    position: absolute; right: 43px; top: 990px;
    font-family: "Montserrat", sans-serif; font-weight: 800; color: var(--ink);
    font-size: 60px; line-height: 1;
  }
  .site-link {
    position: absolute; left: 662px; top: 1097px; width: 494px; height: 50px;
    border-radius: 25px; background: var(--blue); color: var(--white);
    font-family: "Montserrat", sans-serif; font-weight: 700; font-size: 27px;
    display: flex; align-items: center; justify-content: center; text-decoration: none;
  }
</style>
</head>
<body>
<main class="post">
  <svg class="post-shapes" width="1200" height="1200" viewBox="0 0 1200 1200">
    <defs>
      <linearGradient id="stadium-tone" x1="0" y1="0" x2="0" y2="1">
        <stop offset="0" stop-color="#0b1222"/>
        <stop offset="0.35" stop-color="#1b4f86"/>
        <stop offset="0.6" stop-color="#2f86d6"/>
        <stop offset="0.78" stop-color="#172536"/>
        <stop offset="0.86" stop-color="#2f6a24"/>
        <stop offset="1" stop-color="#1f4d18"/>
      </linearGradient>
      <radialGradient id="ball-tone" cx="0.4" cy="0.4" r="0.6">
        <stop offset="0" stop-color="#ffffff"/>
        <stop offset="0.7" stop-color="#9fb8de"/>
        <stop offset="1" stop-color="#27457e"/>
      </radialGradient>
    </defs>
    <rect class="panel" width="1200" height="1200" fill="var(--panel)"/>
    <polygon class="hero-photo" role="img" aria-label="Footballer in red and white kit kicking under stadium floodlights on a night pitch" points="0,0 412,0 636,1200 0,1200" fill="url(#stadium-tone)"/>
    <polygon class="edge-stripe" points="412,0 421,0 648,1200 636,1200" fill="var(--amber)"/>
    <polygon class="profit-band" points="536,497 1200,497 1200,635 562,635" fill="var(--amber)"/>
    <circle class="football" role="img" aria-label="Football" cx="636" cy="798" r="53" fill="url(#ball-tone)"/>
  </svg>

  <div class="brand-name">Ambervale<br>Kinship</div>

  <section class="feature feature--start">
    <h2 class="feature-title">Start Straight Away</h2>
    <p class="feature-note">(A club can start raising money straight away.)</p>
  </section>
  <section class="feature feature--income">
    <h2 class="feature-title">Sustainable Income</h2>
    <p class="feature-note">(The average player plays for 7 years)</p>
  </section>

  <div class="divider"></div>
  <h2 class="reach-title">FUNDRAISING REACH</h2>

  <div class="profit-figure">50<sup>%</sup></div>
  <p class="profit-text">of the sales is<br>guaranteed profit</p>

  <div class="jackpot-amount"><sup>£</sup>25,000</div>
  <div class="jackpot-label">JACKPOT</div>
  <p class="entry-price">(It costs just <sup>£</sup>1 per week to enter)</p>

  <h2 class="cta">Help Your Club</h2>
  <a class="site-link" href="https://www.ambervalekinship.com">www.ambervalekinship.com</a>
</main>
</body>
</html>
```